KTV Consulting

Government/Entitlement Consulting Services- I assist developers obtain entitlements from local, state and federal government agencies so that they can build their projects. Often these projects are very complicated and political and may face community opposition.

Target Market(s)

Real Estate Developers

Industry/Entity Type

Business Consultant

Contact Information for Business Card

Dana Pelletier
Principal

Font styles to use
Serif
Sans Serif

Requirements
Must have
• Classy and professional appeal.
Nice to have
• I like a combination of a mat and glossy finish. I've seen that done with black and then a bold color for a pop, but am not 100% committed to that.

```html
<!DOCTYPE html>
<html lang="en">
<head>
<meta charset="utf-8">
<title>KTV Consulting – Business Card</title>
<link href="https://fonts.googleapis.com/css2?family=Tinos:wght@400;700&family=Arimo:wght@400&display=swap" rel="stylesheet">
<style>
  :root {
    --backdrop: #2a2421;
    --card: #141414;
    --card-edge: #0b0b0b;
    --ink: #f2f2f2;
    --muted: #cfcfcf;
    --accent: #e8692c;
    --silver: #c9c9c9;
    --rule: #8a8a8a;
  }
  * { margin: 0; padding: 0; box-sizing: border-box; }
  html, body { width: 1200px; height: 900px; overflow: hidden; }
  body {
    background: var(--backdrop);
    position: relative;
    font-family: "Arimo", Arial, sans-serif;
    color: var(--ink);
  }
  .card {
    position: absolute;
    top: 300px;
    width: 520px;
    height: 300px;
    background: var(--card);
    border: 1px solid var(--card-edge);
    border-radius: 3px;
    box-shadow: 0 12px 30px rgba(0,0,0,.45);
  }
  .card--front { left: 50px; }
  .card--back { left: 630px; }

  /* Front */
  .brand-mark {
    position: absolute;
    left: 40px; top: 62px;
    width: 160px;
    text-align: center;
  }
  .brand-mark__ring {
    width: 96px; height: 96px;
    margin: 0 auto 14px;
    border: 2px solid var(--accent);
    border-radius: 50%;
  }
  .brand-mark__name {
    font-family: "Tinos", "Times New Roman", serif;
    font-weight: 700;
    font-size: 17px;
    color: var(--ink);
  }
  .divider {
    position: absolute;
    left: 228px; top: 62px;
    width: 1px; height: 130px;
    background: var(--rule);
  }
  .contact {
    position: absolute;
    left: 250px; top: 58px;
  }
  .contact__name {
    font-family: "Tinos", "Times New Roman", serif;
    font-weight: 700;
    font-size: 19px;
    color: var(--ink);
  }
  .contact__title {
    font-family: "Tinos", "Times New Roman", serif;
    font-size: 13px;
    color: var(--accent);
    margin-bottom: 6px;
  }
  .contact__list { list-style: none; }
  .contact__item {
    display: flex;
    align-items: center;
    gap: 9px;
    font-size: 13px;
    line-height: 19px;
    color: var(--muted);
  }
  .contact__icon { width: 12px; height: 12px; fill: none; stroke: var(--muted); stroke-width: 1.4; }
  .address {
    position: absolute;
    left: 0; right: 0; bottom: 30px;
    text-align: center;
    font-size: 13px;
    color: var(--muted);
  }

  /* Back */
  .back-mark {
    position: absolute;
    inset: 0;
    display: flex;
    flex-direction: column;
    align-items: center;
    justify-content: center;
  }
  .back-mark__ring {
    width: 80px; height: 80px;
    border: 2px solid var(--silver);
    border-radius: 50%;
    margin-bottom: 14px;
  }
  .back-mark__name {
    font-family: "Tinos", "Times New Roman", serif;
    font-weight: 700;
    font-size: 26px;
    letter-spacing: 1px;
    text-transform: uppercase;
    color: var(--silver);
  }
  .back-mark__tagline {
    margin-top: 4px;
    font-family: "Tinos", "Times New Roman", serif;
    font-variant: small-caps;
    font-size: 12px;
    letter-spacing: .5px;
    color: var(--silver);
  }
</style>
</head>
<body>
  <section class="card card--front" aria-label="Business card front">
    <div class="brand-mark">
      <div class="brand-mark__ring"></div>
      <div class="brand-mark__name">KTV Consulting</div>
    </div>
    <div class="divider"></div>
    <div class="contact">
      <div class="contact__name">Dana Pelletier</div>
      <div class="contact__title">Principal</div>
      <ul class="contact__list">
        <li class="contact__item">
          <svg class="contact__icon" viewBox="0 0 12 12"><path d="M2.5 1.5l2 0 .8 2.4-1.2 1c.7 1.4 1.6 2.3 3 3l1-1.2 2.4.8 0 2c-4.5.5-8.5-3.5-8-8z"/></svg>
          555-014-2207
        </li>
        <li class="contact__item">
          <svg class="contact__icon" viewBox="0 0 12 12"><rect x="3" y="1" width="6" height="3"/><rect x="1" y="4" width="10" height="5"/><rect x="3" y="7" width="6" height="4"/></svg>
          555-014-2291
        </li>
        <li class="contact__item">
          <svg class="contact__icon" viewBox="0 0 12 12"><rect x="1" y="2.5" width="10" height="7"/><path d="M1 2.5l5 4 5-4"/></svg>
          ktvconsulting@mail.com
        </li>
        <li class="contact__item">
          <svg class="contact__icon" viewBox="0 0 12 12"><rect x="1" y="1.5" width="10" height="7"/><path d="M4 11h4M6 8.5v2.5"/></svg>
          ktvconsulting.com
        </li>
      </ul>
    </div>
    <p class="address">PO Box 3306, 14 Harbor Lane, Easton, Ma. 02375</p>
  </section>

  <section class="card card--back" aria-label="Business card back">
    <div class="back-mark">
      <div class="back-mark__ring"></div>
      <div class="back-mark__name">KTV Consulting</div>
      <div class="back-mark__tagline">Government/Entitlement Consulting Services</div>
    </div>
  </section>
</body>
</html>
```